Website Design Brief for KBR LEGAL PTY LTD

Company Name: KBR LEGAL PTY LTD

Industry: Legal Services

Target Audience:

Corporate clients
Business owners
Individuals seeking legal advice in Commercial Law, Mergers and Acquisitions, Will Law, Property Law, and Conveyancing
Objective:

To create a professional, user-friendly website that establishes trust and authority in the legal field.
Provide easy access to information about the firm’s services, team, and areas of expertise.
Include client testimonials, contact information, and a blog or resource section for legal insights.
Key Features and Pages:

Homepage:

Clean, modern design with a professional feel.
Introduction to KBR LEGAL with a brief overview of services.
High-quality images or illustrations related to law and professionalism.
Prominent call-to-action (CTA) like "Get in Touch" or "Book a Consultation."
About Us:

Information about the firm's mission, values, and team.
Highlight the expertise and experience of key members.
Include a brief company history, if relevant.
Services:

Detailed descriptions of services, categorized by legal areas (e.g., Commercial Law, Mergers & Acquisitions, Property Law, etc.).
Call-to-action buttons to encourage potential clients to reach out for consultations.
Team:

Profiles of key team members, including their qualifications, expertise, and professional photos.
Include links to their professional networks (LinkedIn).
Testimonials:

Section showcasing positive client testimonials or case studies.
This can help build trust and credibility with potential clients.
Blog or Resources:

A blog or resources section providing legal tips, industry news, and insights.
Content should demonstrate the firm’s knowledge and thought leadership.
Contact Us:

Easy-to-use contact form.
Include phone number, email, physical office address, and possibly a map.
Option for booking consultations or initial meetings directly online.
Client Portal (optional):

Secure login for clients to access their case information, documents, and updates (this could be an advanced feature to consider after launch).
Design Aesthetic:

Clean, modern, and professional.
Elegant use of fonts and a color palette that reflects trust, authority, and sophistication (dark blues, whites, grays).
User-friendly navigation to ensure clients can easily find the information they need.
Technical Considerations:

The website should be mobile-responsive and look great on all devices (desktop, tablet, mobile).
Ensure fast load times and optimized images.
Implement SEO best practices to improve search engine rankings.
Easy-to-update CMS (WordPress or similar) to allow easy future updates.
Competitor/Inspirational Websites:

[Provide examples of legal firms' websites you like, or any designs that reflect the feel you want for your firm.]
Additional Information:

Please ensure all content is aligned with the firm's professional tone and approach.
The website should be designed to be scalable for future growth (adding more services, resources, etc.).

Target Market(s)

Business owners Individuals seeking legal advice in Commercial Law, Mergers and Acquisitions, Will Law, Property Law, and Conveyancing

Industry/Entity Type

Legal

Number of Pages Required

3 page

Requirements
Must have
• Home Page, About Us, Contact Us, Services

```html
<!DOCTYPE html>
<html lang="en">
<head>
<meta charset="utf-8">
<title>KBR LEGAL</title>
<link href="https://fonts.googleapis.com/css2?family=Montserrat:wght@400;500;600;700&display=swap" rel="stylesheet">
<style>
:root{
  --navy:#0f1d40;
  --navy-2:#1b2a52;
  --grey:#8e8e8e;
  --grey-btn:#9a9a9a;
  --light:#f0f0f0;
  --line:#d6d6d6;
  --text:#222;
  --muted:#6b6b6b;
  --white:#fff;
}
*{box-sizing:border-box;margin:0;padding:0}
html,body{width:1200px;height:5000px;overflow:hidden}
body{position:relative;font-family:"Montserrat",sans-serif;color:var(--text);background:var(--white)}
.abs{position:absolute}
.btn{position:absolute;background:var(--grey-btn);color:#fff;font-size:12px;font-weight:500;text-transform:uppercase;display:flex;align-items:center;justify-content:center;letter-spacing:.3px}
.eyebrow{font-size:13px;text-transform:uppercase;color:#444;letter-spacing:.3px}
.h2{font-size:30px;font-weight:700;text-transform:uppercase;line-height:1.3;color:#111;white-space:nowrap}
.img{position:absolute}

/* hero */
.hero{left:0;top:0;width:1200px;height:784px;background:linear-gradient(90deg,#6c6a66 0%,#817f7b 40%,#c9c6c1 70%,#a6a4a0 100%)}
.hero-person{left:520px;top:140px;width:560px;height:644px;background:linear-gradient(180deg,#bdb8b2,#2b2b2e 70%);border-radius:280px 280px 0 0;opacity:.55}
.topbar{left:290px;top:29px;width:820px;height:31px;background:var(--navy);color:#fff;font-size:12px;display:flex;align-items:center;justify-content:space-between;padding:0 40px}
.topbar span{display:flex;align-items:center;gap:8px}
.header{left:89px;top:60px;width:1021px;height:88px;background:#fff;display:flex;align-items:center;padding:0 26px}
.logo{font-size:38px;font-weight:500;color:#111;letter-spacing:1px}
.nav{display:flex;gap:32px;margin-left:60px;font-size:12px;color:#444;text-transform:uppercase}
.header .btn{position:static;margin-left:auto;width:206px;height:38px}
.hero-title{left:89px;top:306px;font-size:58px;font-weight:700;color:#fff;line-height:1.17;text-transform:uppercase}
.dots{left:574px;top:738px;display:flex;gap:6px}
.dots i{width:12px;height:12px;border-radius:50%;background:rgba(255,255,255,.6)}
.dots i.on{background:#fff}

/* features */
.features{left:150px;top:784px;width:900px;height:97px;border:2px solid var(--line);border-top:none;background:#fff;display:flex}
.feature{flex:1;display:flex;align-items:center;justify-content:center;gap:16px;font-size:14px;font-weight:500;text-transform:uppercase;line-height:1.5;border-right:2px solid var(--line)}
.feature:last-child{border-right:none}

/* about */
.about-a{left:138px;top:1000px;width:292px;height:128px;background:linear-gradient(135deg,#8a6b4a,#c9a57c)}
.about-b{left:262px;top:1128px;width:295px;height:362px;background:linear-gradient(160deg,#3a2a1f,#6b4426 50%,#a86a34)}
.about-c{left:138px;top:1128px;width:124px;height:362px;background:linear-gradient(135deg,#2c3a44,#7d8a90)}
.exp-band{left:138px;top:1315px;width:124px;height:175px;background:var(--grey);color:#fff}
.exp-band div{position:absolute;left:22px;bottom:18px;transform:rotate(-90deg);transform-origin:left bottom;white-space:nowrap;display:flex;align-items:flex-end;gap:8px;translate:28px 0}
.exp-band b{font-size:34px;font-weight:500}
.exp-band span{font-size:13px;padding-bottom:6px}
.about-icon{left:460px;top:1005px;width:94px;height:94px;border-radius:50%;background:#e8e8e8;display:flex;align-items:center;justify-content:center}
.about-text{left:618px;top:1036px;width:450px}
.about-text .h2{margin-top:8px}
.about-text p{font-size:12px;color:var(--muted);line-height:1.8;margin-top:12px}
.skills{left:620px;top:1250px;width:440px;height:122px;border:2px solid #999;padding:22px 24px}
.skill{margin-bottom:22px}
.skill .row{display:flex;justify-content:space-between;font-size:13px;font-weight:600;margin-bottom:8px}
.bar{height:4px;background:#ddd}
.bar i{display:block;height:4px;background:var(--navy)}
.about-btn{left:620px;top:1400px;width:158px;height:38px}

/* services */
.svc-title{left:0;top:1598px;width:1200px;text-align:center}
.card{position:absolute;top:1664px;width:256px;height:356px;background:#fff;box-shadow:0 2px 14px rgba(0,0,0,.12);border:1px solid #eee}
.card-in{position:absolute;left:20px;top:22px;width:216px;height:314px;border:1px solid #999;background:#fff;text-align:center}
.card-in .ic{width:58px;height:58px;margin:0 auto;background:var(--navy);display:flex;align-items:center;justify-content:center}
.card-in h3{font-size:13px;font-weight:600;text-transform:uppercase;margin-top:20px}
.card-in p{font-size:12px;color:var(--muted);line-height:1.7;margin:8px 22px 0}
.card-in .photo{position:absolute;left:0;bottom:0;width:100%;height:122px}
.arrow-c{position:absolute;left:50%;margin-left:-18px;width:36px;height:36px;border-radius:50%;background:var(--navy);display:flex;align-items:center;justify-content:center;z-index:2}
.card.dark{border-color:#bbb}
.card.dark .card-in{background:linear-gradient(180deg,#1e2c52,#2d3a5e);border:none;color:#fff}
.card.dark p{color:#fff}
.card.dark .ic{background:#8d8d8d;margin-top:62px}

/* case study */
.case-bg{left:0;top:2138px;width:1200px;height:380px;background:var(--light)}
.case-deco-l{left:0;top:2138px;width:230px;height:380px;background:linear-gradient(90deg,#cfc9c0,#ece9e4);opacity:.8}
.case-deco-r{left:930px;top:2138px;width:270px;height:200px;background:linear-gradient(270deg,#d9d3ca,var(--light));opacity:.8}
.case-text{left:233px;top:2190px}
.case-text .h2{margin-top:8px}
.case-btn{left:953px;top:2217px;width:158px;height:36px}
.case-img{top:2334px;width:233px;height:302px}
.case-tag{left:485px;top:2334px;width:233px;height:327px;background:linear-gradient(180deg,#3a2416,#6b3d1c 60%,#2b1b10)}
.tag-circle{position:absolute;left:36px;top:80px;width:162px;height:162px;border-radius:50%;background:var(--navy);color:#fff;text-align:center;font-size:12px;padding-top:48px;line-height:1.6}
.tag-circle b{font-weight:600;text-transform:uppercase}
.tag-circle .arrow-c{left:50%;top:110px;background:#8d8d8d;width:34px;height:34px}

/* faq */
.faq-text{left:146px;top:2780px}
.faq-text .h2{margin-top:8px}
.faq{left:146px;top:2903px;width:423px}
.faq-item{border:2px solid #d9d9d9;height:48px;display:flex;align-items:center;margin-bottom:14px;font-size:12px;font-weight:600;text-transform:uppercase}
.faq-item .n{width:46px;height:100%;display:flex;align-items:center;justify-content:center;border-right:2px solid #d9d9d9}
.faq-item .q{padding-left:16px}
.faq-open{border:2px solid #d9d9d9;margin-bottom:14px}
.faq-open .head{height:48px;background:var(--grey);color:#fff;display:flex;align-items:center;font-size:12px;font-weight:600;text-transform:uppercase}
.faq-open .head .n{width:46px;text-align:center;border-right:2px solid #aaa;height:100%;display:flex;align-items:center;justify-content:center}
.faq-open .head .q{padding-left:16px}
.faq-open p{font-size:11px;color:var(--muted);line-height:1.75;padding:18px 28px 20px}
.faq-img1{left:674px;top:2780px;width:312px;height:220px;background:linear-gradient(135deg,#3b3128,#8c7a63 60%,#c8b79c)}
.faq-img2{left:830px;top:3000px;width:221px;height:245px;background:linear-gradient(180deg,#e0b263,#a37431 60%,#6d4a1e)}
.faq-img3{left:690px;top:3060px;width:140px;height:170px;background:radial-gradient(circle at 50% 60%,#c99744,#fff 70%)}
.sq{position:absolute;width:24px;height:24px}

/* contact */
.contact-bg{left:233px;top:3367px;width:967px;height:468px;background:var(--light)}
.contact-face{left:1000px;top:3367px;width:200px;height:468px;background:linear-gradient(90deg,var(--light),#d8d8d8)}
.contact-text{left:268px;top:3430px}
.contact-text .h2{margin-top:8px}
.contact-img{left:151px;top:3567px;width:416px;height:264px;background:linear-gradient(135deg,#2a2520,#6e5c48 55%,#3c3128)}
.info{left:196px;top:3626px;width:371px;height:258px;background:#fff;padding:28px 0 0 28px}
.info-row{display:flex;gap:22px;margin-bottom:22px}
.info-row .ci{width:44px;height:44px;border-radius:50%;background:#e6e6e6;display:flex;align-items:center;justify-content:center;flex:none}
.info-row small{display:block;font-size:12px;color:var(--muted);text-transform:uppercase}
.info-row span{font-size:13px;color:var(--muted);line-height:1.6}
.form-frame{left:651px;top:3424px;width:360px;height:386px;background:var(--navy)}
.form{left:629px;top:3443px;width:361px;height:353px;background:#fff;padding:40px 30px 0}
.field{font-size:11px;line-height:14px;text-transform:uppercase;color:#444;border-bottom:1px solid #aaa;padding-bottom:8px;margin-bottom:26px}
.form .btn{left:125px;top:296px;width:110px;height:34px}

/* team */
.team-text{left:0;top:4000px;width:1200px;text-align:center}
.team-text .h2{margin-top:8px}
.member{position:absolute;top:4132px;width:266px;height:340px;border:2px solid #ccc;background:#fff}
.member .ph{position:absolute;left:20px;top:20px;width:222px;height:300px}
.member .mk{position:absolute;left:0;bottom:0;width:20px;height:20px;background:var(--navy)}
.member .nm{position:absolute;left:20px;top:262px;width:160px;height:58px;background:var(--navy);color:#fff;font-size:12px;font-weight:600;text-transform:uppercase;padding:14px 0 0 16px;line-height:1.4}

/* footer */
.footer{left:0;top:4590px;width:1200px;height:410px;background:var(--navy);color:#fff}
.f-logo{position:absolute;left:89px;top:162px;font-size:38px;font-weight:500;letter-spacing:1px}
.f-col{position:absolute;top:80px}
.f-col h4{font-size:20px;font-weight:600;text-transform:uppercase;margin-bottom:14px}
.f-col a{display:block;font-size:12px;text-transform:uppercase;margin-bottom:10px;color:#fff;text-decoration:none}
.f-item{display:flex;gap:10px;font-size:12px;line-height:1.5;margin-bottom:12px}
.f-col p{font-size:12px;line-height:1.6;width:230px}
.sub{margin-top:16px;width:214px;height:44px;background:var(--navy-2);display:flex;align-items:center;padding:0 16px;font-size:11px;gap:10px;border:1px solid #2e3d66}
.sub svg:last-child{margin-left:auto}
.f-rule{position:absolute;left:89px;top:370px;width:1021px;height:1px;background:#3a4870}
.copy{position:absolute;left:0;top:380px;width:1200px;text-align:center;font-size:12px}
.totop{position:absolute;left:1132px;top:346px;width:38px;height:38px;border-radius:50%;background:#8d8d8d;display:flex;align-items:center;justify-content:center}
</style>
</head>
<body>

<!-- Hero -->
<section class="abs hero" role="img" aria-label="Photo of a confident senior female lawyer in a dark blazer in an office">
  <div class="abs hero-person"></div>
</section>
<div class="abs topbar">
  <span><svg width="12" height="12" viewBox="0 0 24 24" fill="#fff"><path d="M6.6 10.8a15 15 0 006.6 6.6l2.2-2.2a1 1 0 011-.25 11.4 11.4 0 003.6.57 1 1 0 011 1V20a1 1 0 01-1 1A17 17 0 013 4a1 1 0 011-1h3.5a1 1 0 011 1c0 1.25.2 2.45.57 3.57a1 1 0 01-.25 1z"/></svg>(123) 456-789</span>
  <span><svg width="13" height="10" viewBox="0 0 24 18" fill="#fff"><path d="M0 0h24v18H0z M2 2l10 7 10-7" stroke="#0f1d40" stroke-width="2"/></svg>help@kbrlegal.example</span>
  <span><svg width="11" height="11" viewBox="0 0 24 24"><circle cx="12" cy="12" r="10" fill="#fff"/><path d="M12 6v6l4 2" stroke="#0f1d40" stroke-width="2" fill="none"/></svg>Mon to Sat: 8.00am-7.00 pm</span>
</div>
<header class="abs header">
  <div class="logo">KBR LEGAL</div>
  <nav class="nav"><span>Home</span><span>About Us</span><span>Services</span><span>Blogs</span><span>Contact Us</span></nav>
  <div class="btn">Book A Consultation</div>
</header>
<h1 class="abs hero-title">Your Defense<br>Is Our Priority,<br>Let Us</h1>
<div class="btn" style="left:89px;top:523px;width:140px;height:38px">Get In Touch</div>
<div class="abs dots"><i></i><i class="on"></i><i></i></div>

<!-- Features -->
<div class="abs features">
  <div class="feature">
    <svg width="44" height="44" viewBox="0 0 44 44" fill="none" stroke="#0f1d40" stroke-width="2"><rect x="4" y="8" width="36" height="32" rx="2"/><path d="M4 16h36M12 4v8M32 4v8"/><circle cx="13" cy="24" r="2"/><circle cx="22" cy="24" r="2"/><circle cx="31" cy="24" r="2"/><circle cx="13" cy="32" r="2"/><circle cx="22" cy="32" r="2"/></svg>
    <span>Book Your<br>Appointment</span></div>
  <div class="feature">
    <svg width="46" height="44" viewBox="0 0 46 44" fill="none" stroke="#0f1d40" stroke-width="2"><rect x="4" y="4" width="28" height="24" rx="2"/><path d="M10 12h16M10 18h12M14 28l-6 8v-8"/><path d="M36 14h6v20h-6v6l-6-6H20v-4"/></svg>
    <span>Get Free<br>Experts Advice</span></div>
  <div class="feature">
    <svg width="44" height="44" viewBox="0 0 44 44" fill="none" stroke="#0f1d40" stroke-width="2"><path d="M4 14L22 4l18 10z M8 18h28M10 18v16M18 18v16M26 18v16M34 18v16M4 38h36"/></svg>
    <span>Best Legal<br>Service Provider</span></div>
</div>

<!-- About -->
<div class="img about-a" role="img" aria-label="Photo of hands signing a document on a wooden desk"></div>
<div class="img about-c" role="img" aria-label="Photo of a legal folder and pen"></div>
<div class="img about-b" role="img" aria-label="Photo of a wooden judge's gavel on an open book"></div>
<div class="abs exp-band"><div><b>20+</b><span>Year Of Experience</span></div></div>
<div class="abs about-icon">
  <svg width="46" height="44" viewBox="0 0 46 44" fill="none" stroke="#0f1d40" stroke-width="2.4"><path d="M4 14L23 4l19 10z M7 18h32M11 18v16M19 18v16M27 18v16M35 18v16M4 38h38"/></svg>
</div>
<div class="abs about-text">
  <div class="eyebrow">About Us</div>
  <h2 class="h2">Best Legal Advisors,<br>Protecting Your Rights</h2>
  <p>There are many variations of passages of lorem ipsum avalab but the majority have suffered alteration in some form, by injected humour, or randomised words which don't</p>
</div>
<div class="abs skills">
  <div class="skill"><div class="row"><span>EXPERIENCE</span><span>70%</span></div><div class="bar"><i style="width:70%"></i></div></div>
  <div class="skill"><div class="row"><span>SUCCESS RATE</span><span>80%</span></div><div class="bar"><i style="width:80%"></i></div></div>
</div>
<div class="btn about-btn">Discover More</div>

<!-- Services -->
<h2 class="abs h2 svc-title">Our Services</h2>
<div class="card" style="left:194px">
  <div class="card-in">
    <div class="ic"><svg width="32" height="32" viewBox="0 0 32 32" fill="none" stroke="#fff" stroke-width="1.8"><path d="M16 4v22M8 8h16M10 28h12M8 8l-4 10h8zM24 8l-4 10h8z"/></svg></div>
    <h3>Commercial Law</h3>
    <p>It is a long established fact that a reader will be distracted...</p>
    <div class="arrow-c" style="top:172px"><svg width="12" height="12" viewBox="0 0 12 12" stroke="#fff" stroke-width="1.6" fill="none"><path d="M2 10L10 2M4 2h6v6"/></svg></div>
    <div class="photo" role="img" aria-label="Photo of a person signing a contract" style="background:linear-gradient(135deg,#2c2520,#b89a7a 60%,#e7ddd0)"></div>
  </div>
</div>
<div class="card dark" style="left:472px">
  <div class="card-in" role="img" aria-label="Photo of a business handshake under a dark blue overlay">
    <div class="ic"><svg width="32" height="32" viewBox="0 0 32 32" fill="none" stroke="#fff" stroke-width="1.8"><rect x="6" y="4" width="20" height="24"/><path d="M10 10h12M10 15h12M10 20h7"/></svg></div>
    <h3>Mergers &amp; Acquisitions</h3>
    <p>It is a long established fact that a reader will be distracted...</p>
    <div class="arrow-c" style="top:250px;background:#8d8d8d"><svg width="12" height="12" viewBox="0 0 12 12" stroke="#fff" stroke-width="1.6" fill="none"><path d="M2 10L10 2M4 2h6v6"/></svg></div>
  </div>
</div>
<div class="card" style="left:750px">
  <div class="card-in">
    <div class="ic"><svg width="32" height="32" viewBox="0 0 32 32" fill="none" stroke="#fff" stroke-width="1.8"><path d="M4 14L16 5l12 9M8 12v16h16V12M13 28v-8h6v8"/></svg></div>
    <h3>Property Law</h3>
    <p>It is a long established fact that a reader will be distracted...</p>
    <div class="arrow-c" style="top:172px"><svg width="12" height="12" viewBox="0 0 12 12" stroke="#fff" stroke-width="1.6" fill="none"><path d="M2 10L10 2M4 2h6v6"/></svg></div>
    <div class="photo" role="img" aria-label="Photo of a property agreement with a small house model" style="background:linear-gradient(135deg,#3a3a3a,#9ea3a8 60%,#dcdcdc)"></div>
  </div>
</div>

<!-- Case study -->
<div class="abs case-bg"></div>
<div class="img case-deco-l" role="img" aria-label="Faded statue of justice"></div>
<div class="img case-deco-r" role="img" aria-label="Faded statue of justice"></div>
<div class="abs case-text">
  <div class="eyebrow">Case Study</div>
  <h2 class="h2">Our Recently Completed<br>Latest Case Study</h2>
</div>
<div class="btn case-btn">Discover More</div>
<div class="img case-img" style="left:233px;background:linear-gradient(180deg,#5a3a22,#9b6a3e 55%,#d4a66c)" role="img" aria-label="Photo of a wood-panelled courtroom"></div>
<div class="img case-tag" role="img" aria-label="Photo of a gavel on a sound block">
  <div class="tag-circle">Utest State<br><b>Domestic Violence</b>
    <div class="arrow-c"><svg width="12" height="12" viewBox="0 0 12 12" stroke="#fff" stroke-width="1.6" fill="none"><path d="M2 10L10 2M4 2h6v6"/></svg></div>
  </div>
</div>
<div class="img case-img" style="left:738px;background:linear-gradient(135deg,#1c2f44,#4b6178 60%,#b08c55)" role="img" aria-label="Photo of a bronze statue of justice"></div>
<div class="img case-img" style="left:988px;width:212px;height:327px;background:linear-gradient(120deg,#d47a2a,#f0c58a 40%,#5a6f86)" role="img" aria-label="Photo of classical columns of a courthouse at sunset"></div>

<!-- FAQ -->
<div class="abs faq-text">
  <div class="eyebrow">FAQs</div>
  <h2 class="h2">Have Questions<br>In Your Mind?</h2>
</div>
<div class="abs faq">
  <div class="faq-item"><span class="n">1</span><span class="q">What H Attorney-Client Privillege?</span></div>
  <div class="faq-item"><span class="n">2</span><span class="q">How Much Does A Lawyer Cost?</span></div>
  <div class="faq-open">
    <div class="head"><span class="n">3</span><span class="q">Can A Lawyer Help Get My Charges Data ?</span></div>
    <p>There are many variations of passages of lorem ipsum available, but the majority have suffered alteradution some form by injected humour,</p>
  </div>
  <div class="faq-item"><span class="n">4</span><span class="q">What Are The Grounds For Divorce?</span></div>
</div>
<div class="img faq-img1" role="img" aria-label="Photo of a female lawyer writing at a desk"></div>
<div class="img faq-img3" role="img" aria-label="Photo of golden scales of justice"></div>
<div class="img faq-img2" role="img" aria-label="Photo of a courthouse facade with columns"></div>
<div class="sq" style="left:1022px;top:2938px;background:var(--navy)"></div>
<div class="sq" style="left:998px;top:2962px;background:#9a9a9a"></div>

<!-- Contact -->
<div class="abs contact-bg"></div>
<div class="img contact-face" role="img" aria-label="Faded photo of a smiling woman"></div>
<div class="abs contact-text">
  <div class="eyebrow">Contact With Us</div>
  <h2 class="h2">Feel Free To<br>Write Us Anytime</h2>
</div>
<div class="img contact-img" role="img" aria-label="Photo of a blindfolded justice statue holding scales"></div>
<div class="abs info">
  <div class="info-row"><div class="ci"><svg width="16" height="16" viewBox="0 0 24 24" fill="#0f1d40"><path d="M6.6 10.8a15 15 0 006.6 6.6l2.2-2.2a1 1 0 011-.25 11.4 11.4 0 003.6.57 1 1 0 011 1V20a1 1 0 01-1 1A17 17 0 013 4a1 1 0 011-1h3.5a1 1 0 011 1c0 1.25.2 2.45.57 3.57a1 1 0 01-.25 1z"/></svg></div><div><small>Phone</small><span>(123) 456-789</span></div></div>
  <div class="info-row"><div class="ci"><svg width="16" height="12" viewBox="0 0 24 18"><path d="M0 0h24v18H0z" fill="#0f1d40"/><path d="M2 2l10 7 10-7" stroke="#e6e6e6" stroke-width="2" fill="none"/></svg></div><div><small>Email Address</small><span>help@kbrlegal.example</span></div></div>
  <div class="info-row"><div class="ci"><svg width="16" height="16" viewBox="0 0 24 24"><circle cx="12" cy="12" r="10" fill="#0f1d40"/><path d="M12 6v6l4 2" stroke="#fff" stroke-width="2" fill="none"/></svg></div><div><small>Timing</small><span>Mon to Sat: 8.00am-7.00 pm</span></div></div>
</div>
<div class="abs form-frame"></div>
<form class="abs form">
  <div class="field">Your Name</div>
  <div class="field">Email Address</div>
  <div class="field">Phone</div>
  <div class="field">Subject</div>
  <div class="field">Message</div>
  <div class="btn">Submit</div>
</form>

<!-- Team -->
<div class="abs team-text">
  <div class="eyebrow">Our Expertise</div>
  <h2 class="h2">Meet Our Experienced<br>Attorney Lawyers</h2>
</div>
<div class="member" style="left:181px">
  <div class="ph" role="img" aria-label="Portrait of a male lawyer in black with arms crossed" style="background:linear-gradient(180deg,#d9d9d9,#7d7d7d 60%,#1e1e1e)"></div>
  <div class="nm">Tom Whitfield<br>Lawyer</div><div class="mk"></div>
</div>
<div class="member" style="left:470px">
  <div class="ph" role="img" aria-label="Portrait of a female lawyer with long brown hair" style="background:linear-gradient(180deg,#e4e4e4,#9c7a62 55%,#2a2a2a)"></div>
  <div class="nm">Laura Benton<br>Lawyer</div><div class="mk"></div>
</div>
<div class="member" style="left:755px">
  <div class="ph" role="img" aria-label="Portrait of a smiling male lawyer in a light blue shirt" style="background:linear-gradient(180deg,#eef0f2,#b7c3d0 55%,#8aa0b8)"></div>
  <div class="nm">Ryan Okafor<br>Lawyer</div><div class="mk"></div>
</div>

<!-- Footer -->
<footer class="abs footer">
  <div class="f-logo">KBR LEGAL</div>
  <div class="f-col" style="left:375px">
    <h4>Quick Links</h4>
    <a>Home</a><a>About Us</a><a>Services</a><a>Team</a><a>Blog</a><a>Contact Us</a>
  </div>
  <div class="f-col" style="left:615px">
    <h4>Contact Info</h4>
    <div class="f-item"><svg width="12" height="10" viewBox="0 0 24 18" fill="#fff"><path d="M0 0h24v18H0z"/></svg><div>EMAIL:<br>help@kbrlegal.example</div></div>
    <div class="f-item"><svg width="12" height="12" viewBox="0 0 24 24" fill="#fff"><path d="M6.6 10.8a15 15 0 006.6 6.6l2.2-2.2a1 1 0 011-.25 11.4 11.4 0 003.6.57 1 1 0 011 1V20a1 1 0 01-1 1A17 17 0 013 4a1 1 0 011-1h3.5a1 1 0 011 1c0 1.25.2 2.45.57 3.57a1 1 0 01-.25 1z"/></svg><div>PHONE:<br>(123) 456-789</div></div>
    <div class="f-item"><svg width="12" height="14" viewBox="0 0 24 30" fill="#fff"><path d="M12 0a10 10 0 00-10 10c0 8 10 20 10 20s10-12 10-20A10 10 0 0012 0zm0 14a4 4 0 110-8 4 4 0 010 8z"/></svg><div>TIMING:<br>Mon to Sat: 8.00am-7.00 pm</div></div>
  </div>
  <div class="f-col" style="left:895px">
    <h4>Newsletter</h4>
    <p>Subscribe to our email address to get the latest news.</p>
    <div class="sub"><svg width="12" height="9" viewBox="0 0 24 18" fill="#fff"><path d="M0 0h24v18H0z"/></svg>Enter Your Email..<svg width="14" height="14" viewBox="0 0 24 24" fill="#fff"><path d="M2 12L22 2l-6 20-4-8z"/></svg></div>
  </div>
  <div class="totop"><svg width="12" height="12" viewBox="0 0 12 12" stroke="#fff" stroke-width="1.8" fill="none"><path d="M2 8l4-4 4 4"/></svg></div>
  <div class="f-rule"></div>
  <div class="copy">©2025 KBR LEGAL | ALL RIGHTS RESERVED</div>
</footer>

</body>
</html>
```